Personal Card: Make it roar!

Hello to all designers,
Hope you're having a nice day/evening! Let's cut to the chase. I would like a modern, beautiful and professional personal business card; with a vector-art of a lion. I'd like the lion to be Blood Red. On a black background. I'm a Filipino, and would love to have my country's flag incorporated into the design. Id like the stars of my flag to be used in your designs if possible. The texts I want on the card are only my name, number, and email address. Colour of my name should be White, and my details Silver. The size and font should be simple and professional, you're in charge of that! The placements of the lion and my details will be yours to decide.

At the back of the card, I would like just the words "Thank You" (Silver) on a Black Background. Right on the center.

To summarise, my requirements are:
- Blood Red: Front Face of Lion, Vector-Art
- Black: Background
- Yellow: Three Stars used in the design
- White: Benedict Sr Talavera
- Silver: Number & Email (Where appropriate)
- Back of the card (Center). Silver: "Thank You"
- Please DON'T use the colour blue.

It's all about the Lion. Images you'll find attached are some images of Lions' faces which I particularly want to be captured and put onto the card. Convert it into a vector-art. A vector-art Lion. PLEASE use the images attached for inspiration only! Do not use it on your designs. Thank you very much for your time.

Good luck!

Ben
Updates

Hello Desginers, Please use Blood Red for the colour red in your designs:HEX: 8A0707RGB: 138,7,7Thank you,Ben Added Saturday, March 12, 2016

Target Market(s)

Potential Connections

Industry/Entity Type

It Professional

Contact Information for Business Card

Name: Benedict Sr Talavera
Email: bentalavera@mailhaven.co.uk
Number: 07382614927

Requirements
Must have
• Modern, Professional & Simple
• (Blood Red HEX: 8A0707, RGB: 138,7,7) Lion (Vector-style art)
• (Black) Background
• (White) My Name
• (Silver) My Details
• Back of card: "Thank You" in Silver. Font size should be small/medium.
• Only colours that should be used are Red, Black, Yellow and White/Silver
Nice to have
• - Use of 3 Yellow stars on the design
Should not have
• - Please avoid using any other colours apart from those specified.

```html
<!DOCTYPE html>
<html lang="en">
<head>
<meta charset="utf-8">
<title>Benedict Sr Talavera – Business Card</title>
<link rel="stylesheet" href="https://fonts.googleapis.com/css2?family=Playfair+Display:wght@400;700&display=swap">
<style>
  :root {
    --backdrop: #d6d6d6;
    --card-black: #050505;
    --blood-red: #8a0707;
    --blood-red-mid: #6a0505;
    --blood-red-deep: #2a0202;
    --star-yellow: #f5c400;
    --name-white: #ffffff;
    --detail-silver: #a9adad;
    --shadow: rgba(0, 0, 0, 0.35);
  }
  * { box-sizing: border-box; margin: 0; padding: 0; }
  html, body {
    width: 1200px;
    height: 960px;
    overflow: hidden;
    background: var(--backdrop);
  }
  .canvas {
    position: relative;
    width: 1200px;
    height: 960px;
  }
  .card {
    position: absolute;
    background: var(--card-black);
    box-shadow: 0 14px 36px var(--shadow);
    font-family: "Playfair Display", Georgia, serif;
    overflow: hidden;
  }
  .card-front {
    left: 60px;
    top: 50px;
    width: 840px;
    height: 500px;
  }
  .card-back {
    left: 690px;
    top: 630px;
    width: 460px;
    height: 280px;
    display: flex;
    align-items: center;
    justify-content: center;
  }
  .lion-banner {
    position: absolute;
    left: 200px;
    top: 60px;
    width: 440px;
    height: 260px;
  }
  .lion-banner .banner-left { fill: url(#bannerFade); }
  .lion-banner .banner-right { fill: url(#bannerFade); }
  .lion-artwork {
    position: absolute;
    left: 280px;
    top: 36px;
    width: 280px;
    height: 300px;
    border-radius: 46% 46% 40% 40% / 42% 42% 58% 58%;
    background:
      radial-gradient(ellipse at 50% 38%, var(--blood-red) 0%, var(--blood-red) 40%, var(--blood-red-mid) 70%, var(--blood-red-deep) 100%);
  }
  .flag-stars {
    position: absolute;
    left: 575px;
    top: 52px;
    width: 90px;
    height: 130px;
  }
  .flag-stars polygon { fill: var(--star-yellow); }
  .card-name {
    position: absolute;
    left: 0;
    right: 0;
    top: 352px;
    text-align: center;
    color: var(--name-white);
    font-weight: 700;
    font-size: 36px;
    line-height: 1.2;
    letter-spacing: 0.22em;
    text-transform: uppercase;
  }
  .card-details {
    position: absolute;
    left: 0;
    right: 0;
    top: 408px;
    text-align: center;
    color: var(--detail-silver);
    font-weight: 400;
    font-size: 17px;
    letter-spacing: 0.12em;
    line-height: 1.6;
    text-transform: uppercase;
  }
  .card-details span { display: block; }
  .thank-you {
    color: var(--detail-silver);
    font-weight: 400;
    font-size: 22px;
    letter-spacing: 0.16em;
    text-transform: uppercase;
  }
</style>
</head>
<body>
<main class="canvas">
  <section class="card card-front">
    <svg class="lion-banner" viewBox="0 0 440 260" aria-hidden="true">
      <defs>
        <linearGradient id="bannerFade" x1="0" y1="0" x2="0" y2="1">
          <stop offset="0" stop-color="#8a0707"/>
          <stop offset="1" stop-color="#3a0303"/>
        </linearGradient>
      </defs>
      <polygon class="banner-left" points="40,40 130,10 150,230 20,200"/>
      <polygon class="banner-right" points="300,20 400,60 420,170 300,220"/>
    </svg>
    <div class="lion-artwork" role="img" aria-label="Blood red vector illustration of a lion's face with an ornate patterned mane"></div>
    <svg class="flag-stars" viewBox="0 0 90 130" aria-hidden="true">
      <polygon points="22,4 27,16 40,16 30,24 34,37 22,29 10,37 14,24 4,16 17,16"/>
      <polygon points="50,38 55,50 68,50 58,58 62,71 50,63 38,71 42,58 32,50 45,50"/>
      <polygon points="62,80 67,92 80,92 70,100 74,113 62,105 50,113 54,100 44,92 57,92"/>
    </svg>
    <h1 class="card-name">Benedict Sr Talavera</h1>
    <p class="card-details">
      <span class="card-phone">07382614927</span>
      <span class="card-email">bentalavera@mailhaven.co.uk</span>
    </p>
  </section>
  <section class="card card-back">
    <p class="thank-you">Thank You</p>
  </section>
</main>
</body>
</html>
```